Business card - mobile service

O KiraTel is a mobile family safety service based on tablets and smartphones.
The business card must have:
BASIC INFO
Company Logo
Name
Position / Job Title: Co-founder
Mobile Phone Number: +55 (11) 5080 6172
Land Line: +55 (11) 9087 614352
Email Address: name@kiratel-example.com
Web Site URL: www.kiratel-example.com
PROMOTIONAL INFO
Try KiraTel free Today!
Your personal promo code: xxxx-2222-uuuu-7777-1234
Promo code text explanation with the instructions about the trial offer
Updates
Dears,
One more must have: the KiraTel slogan:
Industry/Entity Type
Safety
Look and feel
Each slider illustrates characteristics of the customer's brand and the style your logo design should communicate.

```html
<!DOCTYPE html>
<html lang="en">
<head>
<meta charset="utf-8">
<title>KiraTel Business Card</title>
<link href="https://fonts.googleapis.com/css2?family=Baloo+2:wght@400;500;600;700;800&display=swap" rel="stylesheet">
<style>
  :root {
    --page-bg: #ffffff;
    --blue-light: #2a9ad8;
    --blue-mid: #1873c4;
    --blue-deep: #0a4fa6;
    --brand-blue: #1188d4;
    --yellow: #ffcc00;
    --yellow-light: #ffe01a;
    --yellow-warm: #ffc20e;
    --white: #ffffff;
    --card-shadow: 0 2px 8px rgba(0,0,0,0.18);
  }
  * { margin: 0; padding: 0; box-sizing: border-box; }
  html, body {
    width: 1200px; height: 900px; overflow: hidden;
    background: var(--page-bg);
    font-family: "Baloo 2", sans-serif;
  }
  .canvas { position: relative; width: 1200px; height: 900px; }

  .card {
    position: absolute; left: 390px; width: 420px; height: 241px;
    border-radius: 22px; overflow: hidden; box-shadow: var(--card-shadow);
  }

  /* Front */
  .card-front {
    top: 163px;
    background: radial-gradient(circle at 22% 30%, var(--blue-light) 0%, var(--blue-mid) 55%, var(--blue-deep) 100%);
  }
  .front-decor { position: absolute; inset: 0; }
  .front-tab {
    position: absolute; left: 395px; top: 32px; width: 30px; height: 178px;
    background: var(--yellow); border-radius: 12px 0 0 12px;
  }
  .brand-mark {
    position: absolute; left: 36px; top: 38px;
    display: flex; align-items: center; gap: 6px;
    font-size: 30px; font-weight: 800; color: var(--white); line-height: 1;
  }
  .brand-dot { width: 12px; height: 12px; border-radius: 50%; background: var(--yellow); }
  .holder {
    position: absolute; right: 33px; top: 62px; text-align: right; line-height: 1.1;
  }
  .holder-name { font-size: 16px; font-weight: 700; color: var(--yellow); }
  .holder-role { font-size: 12px; font-weight: 500; color: var(--white); }
  .contacts {
    position: absolute; right: 33px; top: 123px; text-align: right;
    list-style: none; line-height: 14px; font-size: 12px; color: var(--white); font-weight: 500;
  }
  .contacts .label { font-size: 10px; color: var(--yellow); margin-right: 3px; }
  .slogan {
    position: absolute; left: 35px; top: 196px;
    font-size: 13.5px; font-weight: 700; color: var(--white);
  }

  /* Back */
  .card-back {
    top: 496px;
    background: linear-gradient(160deg, var(--yellow-warm) 0%, var(--yellow) 50%, var(--yellow-light) 100%);
  }
  .back-decor { position: absolute; inset: 0; }
  .offer {
    position: absolute; left: 0; right: 0; top: 72px; text-align: center;
    font-size: 28px; font-weight: 800; color: var(--brand-blue); letter-spacing: -0.3px;
  }
  .offer-free {
    display: inline-block; color: var(--white); font-style: italic; font-weight: 700;
    transform: rotate(-12deg) translateY(-8px); margin: 0 2px;
  }
  .promo {
    position: absolute; left: 0; right: 0; top: 162px; text-align: center;
    font-size: 10.5px; line-height: 12px; color: var(--brand-blue); font-weight: 500;
  }
  .promo-code-label { color: var(--white); font-weight: 700; }
  .promo-code { font-weight: 700; }
</style>
</head>
<body>
<main class="canvas">

  <section class="card card-front" aria-label="Business card front">
    <svg class="front-decor" width="420" height="241" viewBox="0 0 420 241" role="img" aria-label="Soft curved mesh texture rising across the lower card">
      <defs>
        <linearGradient id="meshBlue" x1="0" y1="1" x2="1" y2="0">
          <stop offset="0" stop-color="#5aa8e6" stop-opacity="0.55"/>
          <stop offset="1" stop-color="#5aa8e6" stop-opacity="0"/>
        </linearGradient>
        <linearGradient id="sweep" x1="0" y1="0" x2="1" y2="0">
          <stop offset="0" stop-color="#ffffff" stop-opacity="0"/>
          <stop offset="1" stop-color="#0c3f8f" stop-opacity="0.35"/>
        </linearGradient>
      </defs>
      <path d="M0 180 C120 140 240 120 330 125 L330 241 L0 241 Z" fill="url(#meshBlue)"/>
      <path d="M250 0 C310 60 330 160 320 241 L420 241 L420 0 Z" fill="url(#sweep)"/>
    </svg>
    <div class="front-tab"></div>
    <div class="brand-mark"><span class="brand-name">KiraTel</span><span class="brand-dot"></span></div>
    <div class="holder">
      <p class="holder-name">Field For Name</p>
      <p class="holder-role">Position / Job Title: Co-founder</p>
    </div>
    <ul class="contacts">
      <li><span class="label">m.phone</span>+55 (11) 5080 6172</li>
      <li><span class="label">phone</span>+55 (11) 9087 614352</li>
      <li><span class="label">email</span>name@kiratel-example.com</li>
      <li><span class="label">web</span>www.kiratel-example.com</li>
    </ul>
    <p class="slogan">Your Family Safety Service</p>
  </section>

  <section class="card card-back" aria-label="Business card back">
    <svg class="back-decor" width="420" height="241" viewBox="0 0 420 241" role="img" aria-label="Soft mesh texture fading from the top left corner">
      <defs>
        <linearGradient id="meshYellow" x1="0" y1="0" x2="1" y2="1">
          <stop offset="0" stop-color="#f5b800" stop-opacity="0.6"/>
          <stop offset="1" stop-color="#f5b800" stop-opacity="0"/>
        </linearGradient>
      </defs>
      <path d="M0 0 L420 0 L420 55 C300 100 150 160 0 241 Z" fill="url(#meshYellow)"/>
    </svg>
    <h2 class="offer">Try KiraTel <span class="offer-free">free</span> today</h2>
    <div class="promo">
      <p><span class="promo-code-label">Promo Code</span> <span class="promo-code">xxxx-2222-uuuu-7777-1234</span></p>
      <p>Promo code text explanation Lorem ipsum dolor sit amet, consectetuer elit.</p>
      <p>Nam nibh. Nunc varius facilisis eros. Sed erat. In in velit quis arcu ornare laoreet.</p>
      <p>Curabitur adipiscing luctus massa. Nunc nec mi eu justo tempor consectetuer.</p>
    </div>
  </section>

</main>
</body>
</html>
```